Tess Marlowe Communication business card

I am starting a small, country-based business that offers writing, communication and marketing services to a wide range of clients, inner city big business, to mining, through to agriculture.

The appeal of my business is that it's mobile and flexible. It's just me, with lots of hands-on experience on construction and infrastructure projects.

I can provide the following services:

• Communication planning and management
• Issues and media management
• Marketing and communication materials
• Project management and strategy
• Government liaison
• Incident management communication
• Stakeholder management

It would be great to be able to use the elements of the business card design on other stationery.

Industry/Entity Type

Communication

Requirements
Must have
• The following information:

Tess Marlowe
M: 0427 391 864
E: tess@tmcommsmail.com

PO Box 152
Durrandale Q 4472
Nice to have
• a rural element (windmill, workboots, wheat stalk)

```html
<!DOCTYPE html>
<html lang="en">
<head>
<meta charset="utf-8">
<title>Tess Marlowe Communication – Business Card</title>
<link rel="stylesheet" href="https://fonts.googleapis.com/css2?family=Open+Sans:wght@400;600;700&display=swap">
<style>
  :root {
    --page: #e9e7e3;
    --card-black: #050608;
    --brand-blue: #3aa3e0;
    --band-blue: #45a8e6;
    --band-blue-deep: #2f8fcf;
    --swoosh-grey: #c9ced3;
    --white: #ffffff;
    --ink-on-blue: #ffffff;
  }
  html, body {
    margin: 0;
    width: 1200px;
    height: 900px;
    overflow: hidden;
    background: var(--page);
    font-family: "Open Sans", Arial, sans-serif;
  }
  .sheet {
    width: 1200px;
    height: 900px;
    display: flex;
    flex-direction: column;
    align-items: center;
    justify-content: center;
    gap: 40px;
  }
  .card {
    position: relative;
    width: 700px;
    height: 400px;
    background: var(--card-black);
    overflow: hidden;
    box-shadow: 0 10px 24px rgba(0,0,0,0.25);
  }
  .card-art {
    position: absolute;
    inset: 0;
    width: 100%;
    height: 100%;
  }
  .wordmark {
    position: absolute;
    display: flex;
    align-items: center;
    gap: 14px;
    color: var(--brand-blue);
    font-weight: 700;
    text-transform: uppercase;
    line-height: 1;
  }
  .wordmark-square {
    width: 34px;
    height: 34px;
    background: var(--brand-blue);
  }
  .wordmark-name { font-size: 36px; letter-spacing: 1px; }
  .wordmark-sub { font-size: 16px; letter-spacing: 5px; margin-top: 6px; }

  /* Contact side */
  .card-contact .wordmark { left: 60px; top: 70px; }
  .contact-row {
    position: absolute;
    left: 0; right: 0; bottom: 46px;
    display: flex;
    align-items: flex-end;
    padding: 0 40px;
    gap: 44px;
    color: var(--ink-on-blue);
    font-size: 14px;
    line-height: 1.5;
  }
  .contact-name { font-size: 21px; font-weight: 700; }
  .contact-block p { margin: 0; }

  /* Services side */
  .card-services .wordmark { left: 40px; bottom: 50px; }
  .services-list {
    position: absolute;
    right: 30px;
    top: 30px;
    width: 290px;
    margin: 0;
    padding-left: 18px;
    color: var(--ink-on-blue);
    font-size: 13px;
    line-height: 1.5;
  }
</style>
</head>
<body>
<main class="sheet">

  <section class="card card-contact" aria-label="Card front with contact details">
    <svg class="card-art" viewBox="0 0 700 400" aria-hidden="true">
      <defs>
        <linearGradient id="bandBlue" x1="0" y1="0" x2="0" y2="1">
          <stop offset="0" stop-color="var(--band-blue)"/>
          <stop offset="1" stop-color="var(--band-blue-deep)"/>
        </linearGradient>
      </defs>
      <path d="M0 262 C 220 250 470 170 700 40 L700 400 L0 400 Z" fill="var(--swoosh-grey)"/>
      <path d="M0 276 C 230 262 480 185 700 62 L700 400 L0 400 Z" fill="var(--card-black)"/>
      <path d="M0 282 C 235 268 485 192 700 72 L700 400 L0 400 Z" fill="var(--white)"/>
      <path d="M0 290 C 240 276 490 202 700 84 L700 400 L0 400 Z" fill="url(#bandBlue)"/>
    </svg>
    <div class="wordmark">
      <span class="wordmark-square"></span>
      <div>
        <div class="wordmark-name">Tess Marlowe</div>
        <div class="wordmark-sub">Communication</div>
      </div>
    </div>
    <div class="contact-row">
      <div class="contact-name">Tess Marlowe</div>
      <div class="contact-block">
        <p>PO Box 152</p>
        <p>Durrandale Q 4472</p>
      </div>
      <div class="contact-block">
        <p>M: 0427 391 864</p>
        <p>E: tess@tmcommsmail.com</p>
      </div>
    </div>
  </section>

  <section class="card card-services" aria-label="Card back with services">
    <svg class="card-art" viewBox="0 0 700 400" aria-hidden="true">
      <defs>
        <linearGradient id="panelBlue" x1="0" y1="0" x2="0" y2="1">
          <stop offset="0" stop-color="var(--band-blue)"/>
          <stop offset="1" stop-color="var(--band-blue-deep)"/>
        </linearGradient>
      </defs>
      <path d="M122 0 C 192 188 440 322 700 354 L700 0 Z" fill="var(--swoosh-grey)"/>
      <path d="M136 0 C 206 180 452 312 700 343 L700 0 Z" fill="var(--card-black)"/>
      <path d="M141 0 C 211 177 455 308 700 338 L700 0 Z" fill="var(--white)"/>
      <path d="M150 0 C 220 170 460 300 700 330 L700 0 Z" fill="url(#panelBlue)"/>
    </svg>
    <ul class="services-list">
      <li>Communication planning and management</li>
      <li>Issues and media management</li>
      <li>Marketing and communication materials</li>
      <li>Project management and strategy</li>
      <li>Government liaison</li>
      <li>Incident management communication</li>
      <li>Stakeholder management</li>
    </ul>
    <div class="wordmark">
      <span class="wordmark-square"></span>
      <div>
        <div class="wordmark-name">Tess Marlowe</div>
        <div class="wordmark-sub">Communication</div>
      </div>
    </div>
  </section>

</main>
</body>
</html>
```